5-star Hotel Web Design Project

I need a custom website design for a 5-star hotel. For full details please look at the attached ZIP archive.

The design should be in layers in Photoshop/Illustrator/InDesign format with all the icons/shapes/maps/graphic assets in vector format (svg, ai, eps) as much as possible.

I prefer white, simple but elegant websites. Please consider the performance/coding experience. We're not making something to show off our design skills on a design contest with fancy parallax effects and confusing animations. We're trying to create usable, functional and clean UI with good UX.

I would like to receive a few option for the color scheme to choose from.

The website will be custom coded, i.e. I'm not using WordPress.

NOTE: Don't bother to submit the generic WordPress style templates. We're looking for something custom made with attention to details. That's why the price is not guaranteed, but don't be mistaken, I'm a long time buyer here on SketchHive and all my projects are paid in full.

Low design quality

Europe

Hotel

5+ page

```html
<!DOCTYPE html>
<html lang="en">
<head>
<meta charset="utf-8">
<title>Solara Resort – Home</title>
<link rel="stylesheet" href="https://fonts.googleapis.com/css2?family=Roboto:wght@400;500;700&family=Cormorant+Garamond:wght@500&display=swap">
<style>
:root{
  --gold:#d2ab67;
  --crimson:#a50d3a;
  --panel:rgba(165,13,58,.86);
  --field:rgba(110,8,40,.55);
  --ink:#1d1d1d;
  --white:#ffffff;
}
*{box-sizing:border-box;margin:0;padding:0}
html,body{width:1200px;height:670px;overflow:hidden}
body{position:relative;font-family:"Roboto",Arial,sans-serif;background:var(--white);color:var(--ink)}
.topbar{position:absolute;left:0;top:0;width:1200px;height:34px;background:var(--gold);color:var(--crimson);font-size:9.5px}
.topbar .item{position:absolute;top:12px;display:flex;align-items:center;gap:6px;white-space:nowrap}
.topbar svg{fill:var(--white)}
.topbar .divider{position:absolute;left:995px;top:0;width:1px;height:34px;background:rgba(255,255,255,.6)}
.header{position:absolute;left:0;top:34px;width:1200px;height:85px;background:var(--white)}
.brand{position:absolute;left:135px;top:24px;display:flex;align-items:center;gap:8px;font-family:"Cormorant Garamond",Georgia,serif;font-weight:500;font-size:24px;color:var(--crimson)}
.brand .dot{width:10px;height:10px;border-radius:50%;background:var(--gold)}
.nav a{position:absolute;top:37px;font-size:10px;letter-spacing:1.2px;color:var(--ink);text-decoration:none;white-space:nowrap}
.nav a.active{left:439px;top:0;width:102px;height:85px;background:var(--crimson);color:var(--white);display:flex;align-items:center;justify-content:center}
.nav a.active::before,.nav a.active::after{content:"";position:absolute;left:40px;width:21px;height:1.5px;background:var(--gold)}
.nav a.active::before{top:26px}.nav a.active::after{top:56px}
.book{position:absolute;left:961px;top:28px;width:108px;height:29px;background:var(--gold);color:var(--crimson);font-size:10px;letter-spacing:.8px;display:flex;align-items:center;justify-content:center;gap:8px}
.hero{position:absolute;left:0;top:119px;width:1200px;height:551px;
  background:linear-gradient(180deg,#8fb0c8 0%,#d9dccf 35%,#b79a6e 52%,#4f6a3a 70%,#3a9aa6 88%,#2b8c99 100%)}
.booking{position:absolute;left:712px;top:217px;width:319px;height:433px;border-radius:26px;background:var(--panel);color:var(--white)}
.label{position:absolute;font-size:10px;font-weight:500;color:#f3dbe0}
.select{position:absolute;height:43px;background:var(--field);font-size:10px;display:flex;align-items:center;padding-left:12px}
.select::after{content:"";position:absolute;right:9px;top:19px;border:4px solid transparent;border-top:4px solid var(--white);border-bottom:0}
.select::before{content:"";position:absolute;right:24px;top:10px;height:23px;border-left:1px dotted rgba(255,255,255,.6)}
.cta-band{position:absolute;left:698px;top:526px;width:348px;height:74px;background:var(--gold)}
.cta{position:absolute;left:89px;top:16px;width:179px;height:39px;border-radius:6px;background:var(--crimson);color:var(--gold);font-weight:700;font-size:15px;display:flex;align-items:center;justify-content:center;letter-spacing:.3px}
.dots span{position:absolute;top:641px;width:14px;height:14px;border-radius:50%;background:#2a2a2a}
.dots span.on{background:var(--crimson)}
</style>
</head>
<body>
<div class="topbar">
  <div class="item" style="left:140px"><svg width="7" height="10" viewBox="0 0 7 10"><circle cx="3.5" cy="3.5" r="3"/><rect x="3" y="5" width="1" height="5"/></svg>45 Harbor Lane Seaview, 000450</div>
  <div class="item" style="left:754px;top:11px"><svg width="10" height="8" viewBox="0 0 10 8"><rect width="10" height="8"/></svg>hello@solarastay.com</div>
  <div class="item" style="left:885px;top:11px"><svg width="9" height="9" viewBox="0 0 9 9"><path d="M1 0h2l1 2-1 1a5 5 0 0 0 3 3l1-1 2 1v2c-5 1-9-3-8-8z"/></svg>+00 555010200</div>
  <div class="divider"></div>
  <div class="item" style="left:1007px;top:11px"><svg width="11" height="11" viewBox="0 0 11 11"><circle cx="5.5" cy="5.5" r="5.5" fill="#3b4f8f"/></svg>ENGLISH<svg width="7" height="4" viewBox="0 0 7 4"><path d="M0 0h7L3.5 4z"/></svg></div>
</div>

<header class="header">
  <div class="brand"><span class="dot"></span>Solara Resort</div>
  <nav class="nav">
    <a class="active" href="#">HOME PAGE</a>
    <a href="#" style="left:561px">SOLARA RESORT</a>
    <a href="#" style="left:675px">SPECIAL OFFERS</a>
    <a href="#" style="left:793px">LOCATION</a>
    <a href="#" style="left:879px">CONTACT</a>
  </nav>
  <div class="book"><svg width="10" height="10" viewBox="0 0 10 10" fill="none" stroke="#a50d3a"><rect x=".5" y="1.5" width="9" height="8"/><line x1=".5" y1="4" x2="9.5" y2="4"/></svg>BOOK NOW</div>
</header>

<div class="hero" role="img" aria-label="Photo of the resort courtyard with pool, palm trees and tropical villas under a blue sky"></div>

<form class="booking">
  <span class="label" style="left:35px;top:41px">Arrival Date:</span>
  <div class="select" style="left:36px;top:56px;width:105px">April</div>
  <div class="select" style="left:155px;top:56px;width:58px">19</div>
  <div class="select" style="left:226px;top:56px;width:67px">2021</div>
  <span class="label" style="left:35px;top:115px">Departure Date:</span>
  <div class="select" style="left:36px;top:128px;width:105px">April</div>
  <div class="select" style="left:155px;top:128px;width:58px">21</div>
  <div class="select" style="left:226px;top:128px;width:67px">2021</div>
  <span class="label" style="left:35px;top:201px">Adults</span>
  <span class="label" style="left:139px;top:202px">Children</span>
  <span class="label" style="left:226px;top:202px">No.of.room</span>
  <div class="select" style="left:37px;top:216px;width:58px">6</div>
  <div class="select" style="left:139px;top:216px;width:58px">2</div>
  <div class="select" style="left:226px;top:216px;width:67px">2</div>
</form>
<div class="cta-band"><div class="cta">CHECK AVAILABILITY</div></div>

<div class="dots"><span class="on" style="left:567px"></span><span style="left:592px"></span><span style="left:619px"></span></div>
</body>
</html>
```